Iron Ridge Roofing Business Card

Need a business card with the logo that was designed here

Contact Information for Business Card

Name, Title, Phone, Email, Website, Company name

```html
<!DOCTYPE html>
<html lang="en">
<head>
<meta charset="utf-8">
<title>Iron Ridge Roofing – Business Card</title>
<link rel="stylesheet" href="https://fonts.googleapis.com/css2?family=Montserrat:wght@700&family=Open+Sans:wght@400;600&display=swap">
<style>
  :root {
    --stage: #2a2a2e;
    --card-dark: #1f1f24;
    --pattern-light: #3a3a40;
    --pattern-dark: #19191d;
    --brand-blue: #1474c4;
    --brand-blue-deep: #0e5a9e;
    --name-grey: #a7a8ac;
    --paper: #ffffff;
    --ink-light: #f2f2f2;
  }
  html, body {
    margin: 0;
    padding: 0;
    width: 1200px;
    height: 780px;
    overflow: hidden;
    background: var(--stage);
  }
  .canvas {
    position: relative;
    width: 1200px;
    height: 780px;
  }
  .card {
    position: absolute;
    top: 230px;
    width: 560px;
    height: 320px;
    overflow: hidden;
    background: var(--card-dark);
    box-shadow: 0 12px 30px rgba(0,0,0,0.45);
  }
  .card--back { left: 30px; }
  .card--front { left: 610px; }

  /* Back */
  .back-pattern {
    position: absolute;
    inset: 0;
    background: linear-gradient(150deg, var(--pattern-light) 0%, var(--pattern-dark) 55%, var(--card-dark) 100%);
  }
  .back-brand {
    position: absolute;
    left: 330px;
    top: 160px;
    display: flex;
    align-items: center;
    gap: 8px;
    font-family: 'Open Sans', sans-serif;
    font-weight: 600;
    font-size: 17px;
    color: var(--brand-blue);
    white-space: nowrap;
  }
  .brand-dot {
    width: 10px;
    height: 10px;
    flex: none;
    background: var(--brand-blue);
  }

  /* Front */
  .front-shape {
    position: absolute;
    inset: 0;
  }
  .name-bar {
    position: absolute;
    left: 28px;
    top: 62px;
    width: 14px;
    height: 62px;
    background: var(--brand-blue);
  }
  .person {
    position: absolute;
    left: 52px;
    top: 58px;
  }
  .person-name {
    margin: 0;
    font-family: 'Montserrat', sans-serif;
    font-weight: 700;
    font-size: 30px;
    line-height: 1.1;
    white-space: nowrap;
  }
  .person-name .first { color: var(--brand-blue); }
  .person-name .last { color: var(--name-grey); }
  .person-title {
    margin: 4px 0 0;
    font-family: 'Open Sans', sans-serif;
    font-weight: 600;
    font-size: 15px;
    color: var(--ink-light);
  }
  .contact {
    position: absolute;
    left: 50px;
    top: 196px;
    font-family: 'Open Sans', sans-serif;
    font-size: 13.5px;
    line-height: 19px;
    color: var(--ink-light);
  }
  .contact p { margin: 0; }
  .contact .address { margin-bottom: 6px; }
  .contact-row {
    display: flex;
    align-items: center;
    gap: 8px;
  }
  .contact-row svg { width: 13px; height: 13px; flex: none; }
  .front-brand {
    position: absolute;
    left: 384px;
    top: 150px;
    width: 168px;
    display: flex;
    align-items: center;
    justify-content: center;
    gap: 7px;
    font-family: 'Open Sans', sans-serif;
    font-weight: 600;
    font-size: 15px;
    color: var(--brand-blue);
    white-space: nowrap;
  }
</style>
</head>
<body>
<main class="canvas">

  <section class="card card--back" aria-label="Card back">
    <div class="back-pattern" role="img" aria-label="Repeating pattern of small house rooflines in shades of grey"></div>
    <div class="back-brand"><span class="brand-dot"></span>Iron Ridge Roofing</div>
  </section>

  <section class="card card--front" aria-label="Card front">
    <svg class="front-shape" viewBox="0 0 560 320" preserveAspectRatio="none" aria-hidden="true">
      <path d="M372 0 C 320 120, 330 270, 400 320 L 560 320 L 560 0 Z" fill="var(--brand-blue)"/>
      <path d="M372 0 C 320 120, 330 270, 400 320 L 412 320 C 352 270, 340 130, 386 0 Z" fill="var(--brand-blue-deep)"/>
      <path d="M398 0 C 350 120, 360 260, 418 320 L 560 320 L 560 0 Z" fill="var(--paper)"/>
    </svg>

    <div class="name-bar"></div>
    <div class="person">
      <h1 class="person-name"><span class="first">Daniel</span> <span class="last">Whitfield</span></h1>
      <p class="person-title">Managing Director</p>
    </div>

    <div class="contact">
      <div class="address">
        <p>1840 Millbrook Ave. Suite 310</p>
        <p>Arlington, TX 76010</p>
      </div>
      <p class="contact-row">
        <svg viewBox="0 0 16 16" aria-hidden="true"><path d="M3 1.5l3 .5 1 3.5-2 1.2a9 9 0 0 0 4.3 4.3L10.5 9l3.5 1 .5 3-2 1.5C6.5 14 2 9.5 1.5 3.5z" fill="var(--brand-blue)"/></svg>
        (555) 214-6037
      </p>
      <p class="contact-row">
        <svg viewBox="0 0 16 16" aria-hidden="true"><rect x="1" y="3" width="14" height="10" rx="1" fill="var(--brand-blue)"/><path d="M1.5 3.5 8 9l6.5-5.5" stroke="var(--card-dark)" stroke-width="1.3" fill="none"/></svg>
        info@ironridgeroof.com
      </p>
      <p class="contact-row">
        <svg viewBox="0 0 16 16" aria-hidden="true"><circle cx="8" cy="8" r="7" fill="var(--brand-blue)"/><path d="M1 8h14M8 1c-3 3.5-3 10.5 0 14M8 1c3 3.5 3 10.5 0 14" stroke="var(--card-dark)" stroke-width="1" fill="none"/></svg>
        www.ironridgeroof.com
      </p>
    </div>

    <div class="front-brand"><span class="brand-dot"></span>Iron Ridge Roofing</div>
  </section>

</main>
</body>
</html>
```